OKRUVI card Technical Architecture

Hello everyone OKRUVI: It is a consulting firm in Architecture and Construction. I require a card duplexing, sober, elegant, classic but not boring. Update 1: Use the following data for the card. Name: Rodrigo Salcedo Mauricio Quintana Position: COO Twitter: @okruviTB Homepage: okruvi.net home address not include the participation of all thank you.

Target Market(s)

Construction companies, Architects and Consulting Engineers

Industry/Entity Type

Consulting

Contact Information for Business Card

Los campos que debe tener:
Nombre, Cargo, email, homepage y twitter

Font styles to use
Serif
Sans Serif
Other font styles liked:
• Me gustan playfair display, open sans y roboto, pero estoy sujeto a sus propuestas

Requirements
Must have
• Colors: Present combined proposals in white, red, gray and black Update 1: The two names must be clearly differentiated from the two surnames
Nice to have
• They are free to present their best proposals. I will bring them immediate feedback to the extent you can go see their designs. Complete data for card and logo files will give the winner the

```html
<!DOCTYPE html>
<html lang="es">
<head>
<meta charset="utf-8">
<title>OKRUVI – Tarjeta de presentación</title>
<link rel="stylesheet" href="https://fonts.googleapis.com/css2?family=Open+Sans:wght@400;600&display=swap">
<style>
  :root {
    --stage: #3b3b3b;
    --paper: #ffffff;
    --brand-red: #8e0d14;
    --deep-red: #640006;
    --bright-red: #c1000d;
    --ink: #1f1f1f;
    --grey-text: #555555;
    --rule: #c9c9c9;
  }
  * { margin: 0; padding: 0; box-sizing: border-box; }
  html, body { width: 1105px; height: 1200px; overflow: hidden; }
  body {
    background: var(--stage);
    font-family: "Open Sans", Arial, sans-serif;
    position: relative;
  }
  .card {
    position: absolute;
    left: 193px;
    width: 718px;
    height: 410px;
  }
  .card--front { top: 146px; background: var(--paper); }
  .card--back {
    top: 602px;
    background: radial-gradient(ellipse 60% 70% at 50% 45%, var(--bright-red) 0%, #9a0008 55%, var(--deep-red) 100%);
  }

  /* front */
  .brand {
    position: absolute;
    left: 55px;
    width: 306px;
    top: 210px;
    text-align: center;
    display: flex;
    align-items: center;
    justify-content: center;
    gap: 14px;
  }
  .brand__mark {
    width: 14px; height: 14px;
    background: var(--brand-red);
  }
  .brand__name {
    font-size: 38px;
    font-weight: 400;
    letter-spacing: 9px;
    color: var(--ink);
    line-height: 1;
  }
  .divider {
    position: absolute;
    left: 378px;
    top: 102px;
    width: 1px;
    height: 207px;
    background: var(--rule);
  }
  .holder {
    position: absolute;
    left: 411px;
    top: 104px;
  }
  .holder__name {
    font-size: 26px;
    font-weight: 600;
    color: var(--brand-red);
    line-height: 31px;
  }
  .holder__role {
    font-size: 19px;
    font-weight: 400;
    color: var(--ink);
    margin-top: 3px;
  }
  .contact {
    list-style: none;
    margin-top: 20px;
  }
  .contact__item {
    display: flex;
    align-items: center;
    gap: 10px;
    font-size: 18px;
    color: var(--grey-text);
    line-height: 28px;
  }
  .contact__icon { width: 17px; height: 17px; flex: none; }

  /* back */
  .back-name {
    position: absolute;
    left: 0; right: 0;
    top: 140px;
    text-align: center;
    font-size: 64px;
    font-weight: 400;
    letter-spacing: 16px;
    color: var(--paper);
  }
  .back-url {
    position: absolute;
    left: 0; right: 0;
    top: 346px;
    text-align: center;
    font-size: 19px;
    letter-spacing: 12px;
    color: var(--paper);
  }
</style>
</head>
<body>
  <section class="card card--front" aria-label="Anverso de la tarjeta">
    <div class="brand">
      <span class="brand__mark"></span>
      <span class="brand__name">OKRUVI</span>
    </div>
    <div class="divider"></div>
    <div class="holder">
      <p class="holder__name">Mauricio Rodrigo<br>Salcedo Quintana</p>
      <p class="holder__role">Director de Operaciones</p>
      <ul class="contact">
        <li class="contact__item">
          <svg class="contact__icon" viewBox="0 0 24 24" aria-hidden="true"><path fill="#8e0d14" d="M6.6 10.8c1.4 2.8 3.8 5.1 6.6 6.6l2.2-2.2c.3-.3.7-.4 1-.2 1.1.4 2.3.6 3.6.6.6 0 1 .4 1 1V20c0 .6-.4 1-1 1C10.6 21 3 13.4 3 4c0-.6.4-1 1-1h3.5c.6 0 1 .4 1 1 0 1.3.2 2.5.6 3.6.1.3 0 .7-.2 1z"/></svg>
          (+571) 555 010 0199
        </li>
        <li class="contact__item">
          <svg class="contact__icon" viewBox="0 0 24 24" aria-hidden="true"><circle cx="12" cy="12" r="9" fill="#8e0d14"/></svg>
          @okruviTB
        </li>
        <li class="contact__item">
          <svg class="contact__icon" viewBox="0 0 24 24" aria-hidden="true"><circle cx="12" cy="12" r="10" fill="#8e0d14"/><path fill="none" stroke="#fff" stroke-width="1.6" d="M2 12h20M12 2c3 3 3 17 0 20M12 2c-3 3-3 17 0 20"/></svg>
          www.okruvi.net
        </li>
      </ul>
    </div>
  </section>

  <section class="card card--back" aria-label="Reverso de la tarjeta">
    <p class="back-name">OKRUVI</p>
    <p class="back-url">www.okruvi.net</p>
  </section>
</body>
</html>
```